BLUE HAVEN (Business Card for Training Company)

Blue Haven is a training and consultancy company with a focus on executive protection and medical. I would like the card to be nice and sharp, not overdone and in black and red. I would also like it to highlight that it is "A Dravin Company"

I would like it to be simple and highlight a few things.

1. Name
2. Title
3. Phone Number
4. Email

I would also like www.dravinholdings.example/blue-haven to be on the card somewhere.

Target Market(s)

Security Companies

Industry/Entity Type

Security

Contact Information for Business Card

Blue Haven is a training and consultancy company with a focus on executive protection and medical. I would like the card to be nice and sharp, not overdone and in black and red. I would also like it to highlight that it is "A Dravin Company" I would like it to be simple and highlight a few things. 1. Name 2. Title 3. Phone Number 4. Email I would also like www.dravinholdings.example/blue-haven to be on the card somewhere.

Requirements
Must have
• A Dravin Company listed on the card and the website
Nice to have
• Highlight Medical Training, Consultancy & Executive Protection Courses

```html
<!DOCTYPE html>
<html lang="en">
<head>
<meta charset="utf-8">
<title>Blue Haven — Business Card</title>
<link rel="stylesheet" href="https://fonts.googleapis.com/css2?family=Archivo:wght@800;900&family=Arimo:wght@400;700&display=swap">
<style>
  :root {
    --stage: #2a2a2c;
    --card-red: #6a0000;
    --card-black: #1b1c1e;
    --ink: #ffffff;
    --pattern-light: #4a4b4e;
    --pattern-dark: #141516;
  }
  * { box-sizing: border-box; margin: 0; padding: 0; }
  html, body {
    width: 1200px; height: 1108px; overflow: hidden;
    background: var(--stage);
  }
  .stage {
    position: relative; width: 1200px; height: 1108px;
    display: flex; justify-content: center; align-items: center; gap: 60px;
  }
  .card {
    position: relative; width: 420px; height: 680px;
    border-radius: 26px; overflow: hidden;
  }
  .card--front {
    background: var(--card-red); color: var(--ink);
    display: flex; flex-direction: column; align-items: center;
    text-align: center; font-family: "Arimo", Arial, sans-serif;
    padding-top: 110px;
  }
  .wordmark {
    font-family: "Archivo", "Arial Black", sans-serif; font-weight: 900;
    font-size: 84px; line-height: 0.9; letter-spacing: -1px;
    text-transform: uppercase;
  }
  .person-name {
    margin-top: 70px;
    font-family: "Archivo", "Arial Black", sans-serif; font-weight: 800;
    font-size: 26px; text-transform: uppercase;
  }
  .person-title { font-size: 19px; margin-top: 4px; }
  .rule { width: 84px; height: 1px; background: var(--ink); margin: 18px 0; }
  .contact { font-size: 19px; line-height: 1.35; }
  .web { font-size: 15px; }
  .parent-line { font-size: 18px; text-transform: uppercase; }
  .parent-name {
    margin-top: 12px; font-family: "Archivo", "Arial Black", sans-serif;
    font-weight: 900; font-size: 34px; text-transform: uppercase;
  }
  .card--back { background: var(--card-black); }
  .back-pattern {
    position: absolute; inset: 0;
    background: linear-gradient(160deg, var(--pattern-light) 0%, #2a2b2e 35%, var(--pattern-dark) 75%);
    opacity: 0.55;
  }
  .back-mark {
    position: absolute; left: 0; right: 0; bottom: 130px; text-align: center;
    color: var(--ink); font-family: "Archivo", "Arial Black", sans-serif;
    font-weight: 900; font-size: 34px; line-height: 0.9; text-transform: uppercase;
  }
</style>
</head>
<body>
<main class="stage">
  <section class="card card--front">
    <h1 class="wordmark">Blue<br>Haven</h1>
    <p class="person-name">Marcus Hale</p>
    <p class="person-title">Managing Director</p>
    <div class="rule"></div>
    <p class="contact">044-987 654 321<br>info@bluehaven.example</p>
    <div class="rule"></div>
    <p class="web">www.dravinholdings.example/blue-haven</p>
    <div class="rule"></div>
    <p class="parent-line">A Dravin Company</p>
    <p class="parent-name">Dravin</p>
  </section>
  <section class="card card--back">
    <div class="back-pattern" role="img" aria-label="Faint repeated company wordmark pattern fading from grey to black"></div>
    <p class="back-mark">Blue<br>Haven</p>
  </section>
</main>
</body>
</html>
```